Visitenkarte erstellen für Reiki Praxis

Visitenkarten für Reiki Praxis Doppelseitig

business cards reiki practice double-sided

The background can also be a different color

```html
<!DOCTYPE html>
<html lang="en">
<head>
<meta charset="utf-8">
<title>Quiet Current Reiki – Business Cards</title>
<link rel="stylesheet" href="https://fonts.googleapis.com/css2?family=Italiana&family=Allura&family=Open+Sans:wght@400;500&display=swap">
<style>
  :root {
    --page-bg: #ecebe6;
    --card-bg: #fdf6f4;
    --ink: #1b1b1b;
    --ink-soft: #5a5450;
    --gold: #c9a233;
    --art-pink: rgba(238, 168, 160, 0.85);
    --art-gold: rgba(222, 198, 140, 0.6);
    --art-fade: rgba(253, 246, 244, 0);
    --shadow: rgba(60, 55, 50, 0.28);
  }
  * { box-sizing: border-box; margin: 0; padding: 0; }
  html, body { width: 933px; height: 1200px; overflow: hidden; }
  body {
    background: var(--page-bg);
    font-family: "Open Sans", Arial, sans-serif;
    color: var(--ink);
    position: relative;
  }
  .card {
    position: absolute;
    left: 230px;
    width: 474px;
    height: 270px;
    border-radius: 28px;
    background: var(--card-bg);
    overflow: hidden;
    box-shadow: 0 6px 18px var(--shadow);
  }
  .card--front { top: 293px; }
  .card--back  { top: 615px; }

  .floral-art { position: absolute; }
  .card--front .floral-art {
    left: 0; top: 0;
    width: 180px; height: 170px;
    background: linear-gradient(150deg, var(--art-pink) 0%, var(--art-gold) 55%, var(--art-fade) 100%);
  }
  .card--back .floral-art {
    left: 0; top: 104px;
    width: 162px; height: 166px;
    background: linear-gradient(30deg, var(--art-pink) 0%, var(--art-gold) 55%, var(--art-fade) 100%);
  }

  .brand-name {
    position: absolute;
    transform: translateX(-50%);
    font-family: "Open Sans", Arial, sans-serif;
    font-weight: 500;
    color: var(--ink);
    white-space: nowrap;
    text-align: center;
    letter-spacing: 0.3px;
    line-height: 1.15;
  }
  .card--front .brand-name { left: 334px; top: 178px; font-size: 18px; }
  .card--back .brand-name  { left: 376px; top: 90px;  font-size: 10px; }

  .practitioner {
    position: absolute;
    transform: translateX(-50%);
    font-family: "Open Sans", Arial, sans-serif;
    font-weight: 500;
    color: var(--ink);
    white-space: nowrap;
    letter-spacing: 3px;
  }
  .card--front .practitioner { left: 334px; top: 202px; font-size: 11px; }
  .card--back .practitioner  { left: 376px; top: 103px; font-size: 6.5px; letter-spacing: 2px; }

  .holder-name {
    position: absolute;
    left: 28px; top: 22px;
    font-family: "Italiana", Georgia, serif;
    font-weight: 400;
    font-size: 36px;
    line-height: 1;
    color: var(--ink);
    letter-spacing: 0.5px;
  }
  .holder-tagline {
    position: absolute;
    left: 28px; top: 70px;
    font-family: "Allura", cursive;
    font-size: 18px;
    color: var(--ink-soft);
  }

  .contact-list {
    position: absolute;
    right: 28px; top: 166px;
    list-style: none;
  }
  .contact-item {
    display: flex;
    align-items: center;
    justify-content: flex-end;
    height: 25px;
    font-size: 12px;
    color: var(--ink);
  }
  .contact-icon {
    width: 17px; height: 17px;
    margin-left: 11px;
    flex: none;
  }
</style>
</head>
<body>

  <section class="card card--front" aria-label="Card front">
    <div class="floral-art" role="img" aria-label="Watercolour flower illustration with gold leaves"></div>
    <p class="brand-name">QUIET CURRENT REIKI</p>
    <p class="practitioner">MIRA SOLDEN</p>
  </section>

  <section class="card card--back" aria-label="Card back">
    <h1 class="holder-name">Lena Marwick</h1>
    <p class="holder-tagline">Reiki Practice</p>
    <p class="brand-name">QUIET CURRENT REIKI</p>
    <p class="practitioner">MIRA SOLDEN</p>
    <div class="floral-art" role="img" aria-label="Watercolour flower illustration with gold leaves"></div>

    <ul class="contact-list">
      <li class="contact-item">
        <span>+123-456-7890</span>
        <svg class="contact-icon" viewBox="0 0 20 20" aria-hidden="true">
          <circle cx="10" cy="10" r="9" fill="none" stroke="var(--ink)" stroke-width="1"/>
          <path d="M7 5.5l1.6 2.2-1 1.2a6 6 0 0 0 3.5 3.5l1.2-1 2.2 1.6-0.9 1.6c-3.8 0-7.2-3.4-7.2-7.2z" fill="var(--gold)"/>
        </svg>
      </li>
      <li class="contact-item">
        <span>hello@reallygreatsite.com</span>
        <svg class="contact-icon" viewBox="0 0 20 20" aria-hidden="true">
          <circle cx="10" cy="10" r="9" fill="none" stroke="var(--ink)" stroke-width="1"/>
          <rect x="5" y="6.5" width="10" height="7" rx="0.8" fill="var(--gold)"/>
          <path d="M5.3 7l4.7 3.7L14.7 7" fill="none" stroke="var(--card-bg)" stroke-width="0.9"/>
        </svg>
      </li>
      <li class="contact-item">
        <span>123 Anywhere St., Any City, ST 1234</span>
        <svg class="contact-icon" viewBox="0 0 20 20" aria-hidden="true">
          <circle cx="10" cy="10" r="9" fill="none" stroke="var(--ink)" stroke-width="1"/>
          <path d="M10 4.5a3.6 3.6 0 0 0-3.6 3.6c0 2.7 3.6 7 3.6 7s3.6-4.3 3.6-7A3.6 3.6 0 0 0 10 4.5z" fill="var(--gold)"/>
          <circle cx="10" cy="8.1" r="1.3" fill="var(--card-bg)"/>
        </svg>
      </li>
    </ul>
  </section>

</body>
</html>
```